Boom Way Hoist Service Business Cards

I need a business card for "Boom Way Hoist and Haulage"

Boomway2023@hoistmail.net

Hoist Works LLC, Boom Way Hoist and Haulage LLC

555.014.7260 | www.BOOMWAYHOISTS.example

Central Indiana & Northeast Ohio

(IN) 14820 Maple Lane Noblesville, IN 46000

(OH) 2450 Pell Street Akron, Ohio 44300

Colors
0094D4
00A9DD
6FCCEA
C7EBF8
E9F6FB
59FF00
82FF00
B8FF75
E3FFCB
F4FFEA
EE7325
F08F49
F5BC92
FAE3D3
FDF4ED
EB3D1F
EC4F4E
F09395
F8D3D4
FCEDEE
E54698
E96AAD
F1A4CE
F9D9EA
FCEFF6
A7469A
B969AE
D3A5CF
EDDBEB
F8F0F9

```html
<!DOCTYPE html>
<html lang="en">
<head>
<meta charset="utf-8">
<title>Boom Way Hoist Service – Business Cards</title>
<link href="https://fonts.googleapis.com/css2?family=Archivo+Black&family=Arimo:wght@400;700&display=swap" rel="stylesheet">
<style>
  :root {
    --canvas: #e4e4e2;
    --card-white: #f4f4f3;
    --card-black: #050505;
    --ink: #111111;
    --ink-light: #f2f2f2;
    --accent: #4cb748;
    --divider: #3a3a3a;
  }
  * { box-sizing: border-box; margin: 0; padding: 0; }
  html, body { width: 1200px; height: 912px; overflow: hidden; background: var(--canvas); }
  body { position: relative; font-family: "Arimo", Arial, sans-serif; }

  .card {
    position: absolute;
    width: 600px;
    height: 343px;
    box-shadow: 0 6px 18px rgba(0,0,0,.18);
    overflow: hidden;
  }

  /* Front */
  .card--front { left: 70px; top: 60px; background: var(--card-white); }
  .front-brand {
    position: absolute; left: 0; right: 0; top: 96px;
    display: flex; align-items: center; justify-content: center; gap: 14px;
  }
  .brand-mark { width: 22px; height: 22px; background: var(--accent); }
  .brand-name {
    font-family: "Archivo Black", "Arial Black", sans-serif;
    font-size: 64px; line-height: 1; letter-spacing: 1px; color: var(--ink);
  }
  .front-url {
    position: absolute; left: 0; right: 0; top: 262px;
    text-align: center; font-size: 15px; letter-spacing: 4px; color: var(--ink);
  }
  .front-url .accent { color: var(--accent); }

  /* Back */
  .card--back { left: 530px; top: 500px; background: var(--card-black); color: var(--ink-light); }
  .back-divider { position: absolute; inset: 0; }
  .back-brand {
    position: absolute; left: 48px; top: 110px;
    display: flex; align-items: center; gap: 10px;
  }
  .back-brand .brand-mark { width: 14px; height: 14px; }
  .back-brand .brand-name { font-size: 40px; color: var(--ink-light); }
  .entities {
    position: absolute; left: 40px; top: 188px; width: 300px;
    text-align: right; font-size: 15px; line-height: 1.3;
  }
  .contact {
    position: absolute; left: 352px; top: 26px; width: 240px;
    font-size: 12.5px; line-height: 1.32;
  }
  .contact__name { font-size: 20px; font-weight: 700; line-height: 1.1; }
  .contact__title { color: var(--accent); font-size: 14px; margin-bottom: 8px; }
  .contact__block { margin-bottom: 8px; }
  .contact__row { display: flex; align-items: center; gap: 7px; }
  .contact__row svg { flex: none; }
  .back-stripe {
    position: absolute; left: 0; right: 0; bottom: 0; height: 30px;
    background: var(--card-white); border-top: 4px solid var(--accent);
  }
</style>
</head>
<body>

<section class="card card--front" aria-label="Business card front">
  <div class="front-brand">
    <span class="brand-mark"></span>
    <span class="brand-name">BOOM WAY</span>
  </div>
  <p class="front-url">www.<span class="accent">BOOMWAYHOISTS</span>.example</p>
</section>

<section class="card card--back" aria-label="Business card back">
  <svg class="back-divider" width="600" height="343" viewBox="0 0 600 343" aria-hidden="true">
    <line x1="320" y1="0" x2="350" y2="309" stroke="var(--divider)" stroke-width="1.5"/>
  </svg>

  <div class="back-brand">
    <span class="brand-mark"></span>
    <span class="brand-name">BOOM WAY</span>
  </div>
  <p class="entities">Hoist Works LLC<br>Boom Way Hoist and Haulage LLC</p>

  <div class="contact">
    <p class="contact__name">Daniel Marsh</p>
    <p class="contact__title">President</p>
    <p class="contact__block">Central Indiana &amp; Northeast Ohio<br>(IN) 14820 Maple Lane<br>Noblesville, IN 46000</p>
    <p class="contact__block">(OH) 2450 Pell Street<br>Akron, Ohio 44300</p>
    <p class="contact__row">
      <svg width="12" height="12" viewBox="0 0 24 24" aria-hidden="true"><path fill="var(--accent)" d="M6.6 10.8a15.1 15.1 0 0 0 6.6 6.6l2.2-2.2c.3-.3.7-.4 1-.2 1.1.4 2.3.6 3.6.6.6 0 1 .4 1 1V20c0 .6-.4 1-1 1A17 17 0 0 1 3 4c0-.6.4-1 1-1h3.5c.6 0 1 .4 1 1 0 1.3.2 2.5.6 3.6.1.3 0 .7-.2 1z"/></svg>
      555.014.7260
    </p>
    <p class="contact__row">
      <svg width="12" height="12" viewBox="0 0 24 24" aria-hidden="true"><rect x="2" y="5" width="20" height="14" fill="var(--accent)"/><path d="M2 5l10 8 10-8" fill="none" stroke="var(--card-black)" stroke-width="2"/></svg>
      Boomway2023@hoistmail.net
    </p>
    <p class="contact__row">
      <svg width="12" height="12" viewBox="0 0 24 24" aria-hidden="true"><circle cx="12" cy="12" r="10" fill="var(--accent)"/><path d="M2 12h20M12 2c3 3 3 17 0 20M12 2c-3 3-3 17 0 20" fill="none" stroke="var(--card-black)" stroke-width="1.5"/></svg>
      www.BOOMWAYHOISTS.example
    </p>
  </div>

  <div class="back-stripe"></div>
</section>

</body>
</html>
```